Updated business card

I would like to change the picture on the existing design. Please use the attached photo. Remove my last name from the logo and have that appear (just my first name with the lock symbol [trademarked]) appear horizontally or vertically? on the front of the card. My company information has changed on the back of the card. It should be "Brindle" instead of "Orbit 58 Fernhollow Realty", 4275 Pellham Blvd. Arlington, VA 22209 is the new address. The Orbit 58 Fernhollow logo should be replaced with the Brindle logo which is attached as well. I am using Zib cards with the rounded edges for printing so the size is larger than the typically business card. The colors should remain consistent with what I have but can be used differently.

```html
<!DOCTYPE html>
<html lang="en">
<head>
<meta charset="utf-8">
<title>Marisol Keating – Business Card</title>
<link href="https://fonts.googleapis.com/css2?family=Montserrat:wght@400;500;700;800&family=Pinyon+Script&display=swap" rel="stylesheet">
<style>
  :root {
    --magenta: #d0168c;
    --magenta-soft: #f2c6df;
    --ink: #141414;
    --paper: #ffffff;
    --stage: #cfd1d3;
    --band-black: #0b0b0b;
  }
  * { box-sizing: border-box; margin: 0; padding: 0; }
  html, body { width: 1200px; height: 1200px; overflow: hidden; }
  body {
    background: var(--stage);
    font-family: "Montserrat", sans-serif;
    color: var(--ink);
    position: relative;
  }
  .card {
    position: absolute;
    top: 250px;
    width: 420px;
    height: 680px;
    border-radius: 18px;
    overflow: hidden;
    background: var(--paper);
    box-shadow: 0 12px 30px rgba(0,0,0,0.18);
  }
  .card-back { left: 150px; }
  .card-front { left: 630px; }

  /* Back side */
  .identity { text-align: center; padding-top: 44px; }
  .identity-name { font-weight: 800; font-size: 18px; letter-spacing: 0.4px; }
  .identity-role {
    font-family: "Pinyon Script", cursive;
    color: var(--magenta);
    font-size: 26px;
    line-height: 1;
    margin-top: 2px;
  }
  .identity-credential { color: var(--magenta); font-size: 14px; margin-top: 2px; }

  .contact-list { list-style: none; margin-top: 10px; }
  .contact-item {
    text-align: center;
    border-top: 1px solid var(--magenta-soft);
    margin: 0 70px;
    padding: 11px 0 10px;
    font-size: 16px;
    white-space: nowrap;
  }
  .contact-item-office { margin: 0 40px; }
  .contact-icon { display: block; margin: 0 auto 6px; width: 32px; height: 32px; }

  .office { text-align: center; font-size: 15px; line-height: 1.3; }
  .office-name { font-weight: 800; font-size: 16px; }
  .office-dot { color: var(--magenta); }

  .brand-band {
    position: absolute; left: 0; right: 0; bottom: 0;
    height: 140px;
    background: var(--magenta);
    display: flex; align-items: center; justify-content: center; gap: 20px;
  }
  .brand-name { font-weight: 500; font-size: 30px; letter-spacing: 5px; color: var(--ink); }
  .brand-rule { width: 1.5px; height: 46px; background: var(--ink); }
  .badge-placeholder { width: 44px; height: 44px; border: 3px solid var(--ink); }

  /* Front side */
  .portrait {
    position: absolute; left: 0; right: 0; top: 0;
    height: 530px;
    background: radial-gradient(ellipse at 45% 40%, #e9b8a0 0%, #b5542c 35%, #6a2e1e 60%, #efeef0 100%);
  }
  .name-band {
    position: absolute; left: 0; right: 0; bottom: 0;
    height: 150px;
    background: var(--band-black);
    color: var(--paper);
    padding: 32px 30px 0 40px;
  }
  .wordmark { font-weight: 400; font-size: 54px; letter-spacing: 3px; line-height: 1; position: relative; display: inline-block; }
  .wordmark-tm { position: absolute; right: -22px; top: -4px; font-size: 11px; letter-spacing: 0; }
  .tagline {
    font-family: "Pinyon Script", cursive;
    font-size: 30px;
    text-align: right;
    margin-top: 4px;
    padding-right: 20px;
  }
</style>
</head>
<body>

<section class="card card-back" aria-label="Card back">
  <header class="identity">
    <p class="identity-name">MARISOL KEATING, J.D., LL.M.</p>
    <p class="identity-role">Realtor</p>
    <p class="identity-credential">Accredited Staging Professional</p>
  </header>

  <ul class="contact-list">
    <li class="contact-item">
      <svg class="contact-icon" viewBox="0 0 34 34" aria-hidden="true">
        <circle cx="17" cy="17" r="17" fill="var(--magenta)"/>
        <path d="M9 13c0-2 3-3 8-3s8 1 8 3v2h-4v-2h-8v2H9z" fill="#fff"/>
        <rect x="11" y="16" width="12" height="8" rx="1.5" fill="#fff"/>
      </svg>
      555.014.2277
    </li>
    <li class="contact-item">
      <svg class="contact-icon" viewBox="0 0 34 34" aria-hidden="true">
        <circle cx="17" cy="17" r="17" fill="var(--magenta)"/>
        <rect x="9" y="11" width="16" height="12" fill="#fff"/>
        <path d="M9 11l8 7 8-7" fill="none" stroke="var(--magenta)" stroke-width="1.4"/>
      </svg>
      Marisol@marisolKeating.com
    </li>
    <li class="contact-item">
      <svg class="contact-icon" viewBox="0 0 34 34" aria-hidden="true">
        <circle cx="17" cy="17" r="17" fill="var(--magenta)"/>
        <g fill="none" stroke="#fff" stroke-width="1.5">
          <circle cx="17" cy="17" r="8"/>
          <ellipse cx="17" cy="17" rx="3.5" ry="8"/>
          <path d="M9 17h16M10.5 13h13M10.5 21h13"/>
        </g>
      </svg>
      MarisolKeating.com
    </li>
    <li class="contact-item contact-item-office">
      <svg class="contact-icon" viewBox="0 0 34 34" aria-hidden="true">
        <circle cx="17" cy="17" r="17" fill="var(--magenta)"/>
        <path d="M17 26s-6-7-6-11a6 6 0 0 1 12 0c0 4-6 11-6 11z" fill="#fff"/>
        <circle cx="17" cy="15" r="2.2" fill="var(--magenta)"/>
      </svg>
      <div class="office">
        <p class="office-name">BRINDLE REALTY</p>
        <p>4275 Pellham Blvd <span class="office-dot">•</span> Arlington, VA 22209</p>
      </div>
    </li>
  </ul>

  <footer class="brand-band">
    <span class="brand-name">BRINDLE</span>
    <span class="brand-rule"></span>
    <span class="badge-placeholder" aria-label="Housing badge"></span>
  </footer>
</section>

<section class="card card-front" aria-label="Card front">
  <div class="portrait" role="img" aria-label="Portrait photo of the agent with long auburn hair against a white backdrop"></div>
  <div class="name-band">
    <p class="wordmark">MARISOL<span class="wordmark-tm">TM</span></p>
    <p class="tagline">Homes, Thoughtfully Found</p>
  </div>
</section>

</body>
</html>
```